Werbeplakat für Frisörsalon
Zielgruppe
Frisörsalon (Coiffeursalon Lindenhof) mit hohem Qualitätsstandard im mittel-hohem Preissegment. Zielgruppe hauptsächlich Frauen (20j - 40j). Jedoch bieten wir auch Herrenfrisuren an.
Aufgabenstellung
Format --> A1
auf erstem Blick erkennbar das es sich um einen Frisörsalon handelt
Text:
erstklassige Damen- und Herrenfrisuren
moderne Kinderfrisuren
Waschen, Schneiden, Föhnen
Färben, Tönung, Mèches
VERANTIQ Behandlung
Hochstecken / Hochzeitsfrisuren / Gala
Warme Farben
Logo auf dem Plakat in Originalfarben
Dame auf dem Plakat mit langem lockigem dichtem Haar (Rotschopf)

```html
<!DOCTYPE html>
<html lang="de">
<head>
<meta charset="utf-8">
<title>Coiffeursalon Lindenhof – Plakat</title>
<link rel="stylesheet" href="https://fonts.googleapis.com/css2?family=Marcellus+SC&display=swap">
<style>
  :root {
    --paper: #ffffff;
    --wine: #6b0303;
    --wine-text: #7a1414;
    --cream: #fde7cb;
    --cream-text: #fbe6c8;
    --warm-light: #e9b57e;
    --warm-mid: #c98a4f;
    --hair-red: #b8321c;
    --hair-dark: #5a2a18;
  }
  * { margin: 0; padding: 0; box-sizing: border-box; }
  html, body { width: 938px; height: 1200px; overflow: hidden; background: var(--paper); }
  .poster {
    position: relative;
    width: 938px;
    height: 1200px;
    background: var(--paper);
    padding: 12px;
    font-family: "Marcellus SC", "Trajan Pro", serif;
  }
  .poster-inner {
    position: relative;
    width: 914px;
    height: 1176px;
    overflow: hidden;
    background: var(--cream);
  }
  .hero-photo {
    position: absolute;
    inset: 0 0 auto 0;
    height: 880px;
    background:
      radial-gradient(ellipse 38% 36% at 50% 40%, var(--hair-red) 0%, rgba(184,50,28,0.75) 45%, rgba(90,42,24,0) 100%),
      radial-gradient(ellipse 60% 55% at 50% 45%, var(--warm-light) 0%, var(--warm-mid) 100%);
  }
  .hero-stripes { position: absolute; inset: 0; width: 914px; height: 880px; }
  .wave { position: absolute; inset: 0; width: 914px; height: 1176px; }
  .brand {
    position: absolute;
    top: 752px;
    left: 0;
    width: 914px;
    text-align: center;
    color: var(--wine);
  }
  .brand-name { font-size: 62px; line-height: 1; letter-spacing: 2px; }
  .brand-sub { font-size: 17px; letter-spacing: 6px; margin-top: 4px; }
  .services {
    position: absolute;
    top: 852px;
    left: 0;
    width: 914px;
    list-style: none;
    text-align: center;
    color: var(--wine-text);
    font-size: 28px;
    line-height: 30px;
    letter-spacing: 0.6px;
  }
  .contact-band {
    position: absolute;
    left: 0;
    bottom: 0;
    width: 914px;
    height: 128px;
    background: var(--wine);
    color: var(--cream-text);
    text-align: center;
  }
  .contact-address { font-size: 26px; letter-spacing: 1px; margin-top: 10px; }
  .contact-phone { font-size: 82px; line-height: 1; letter-spacing: 3px; margin-top: 2px; }
</style>
</head>
<body>
  <main class="poster">
    <div class="poster-inner">
      <div class="hero-photo" role="img" aria-label="Porträtfoto einer Frau mit vollem, lockigem Haar in Rot-, Kupfer- und Brauntönen vor warmem Hintergrund"></div>
      <svg class="hero-stripes" viewBox="0 0 914 880" aria-hidden="true">
        <rect x="113" y="0" width="115" height="880" fill="#3a1a0e" opacity="0.12"/>
        <rect x="373" y="0" width="110" height="880" fill="#3a1a0e" opacity="0.10"/>
        <rect x="666" y="0" width="115" height="880" fill="#3a1a0e" opacity="0.12"/>
      </svg>
      <svg class="wave" viewBox="0 0 914 1176" aria-hidden="true">
        <path d="M0,800 C150,720 300,590 460,585 C600,582 650,770 740,775 C820,780 880,745 914,735 L914,1176 L0,1176 Z" fill="var(--wine)"/>
        <path d="M0,852 C150,780 300,650 460,648 C590,646 640,790 740,795 C820,798 880,768 914,760 L914,1176 L0,1176 Z" fill="var(--cream)"/>
      </svg>
      <div class="brand">
        <div class="brand-name">Lindenhof</div>
        <div class="brand-sub">COIFFEURSALON</div>
      </div>
      <ul class="services">
        <li>ERSTKLASSIGE DAMEN- UND HERRENFRISUREN</li>
        <li>MODERNE KINDERFRISUREN</li>
        <li>WASCHEN, SCHNEIDEN, FÖHNEN</li>
        <li>FÄRBEN, TÖNUNG, MÈCHES</li>
        <li>VERANTIQ BEHANDLUNG</li>
        <li>HOCHSTECKEN / HOCHZEITSFRISUREN / GALA</li>
      </ul>
      <div class="contact-band">
        <p class="contact-address">LINDENWEG 12 | 3999 FICHTENTAL</p>
        <p class="contact-phone">031 555 01 23</p>
      </div>
    </div>
  </main>
</body>
</html>
```